K.L.T Services

We are needing business cards for a construction company that does everything from painting and detailing, maintenance, Sheetrock repairs, demolition, tile and wood floors. Also, K.L.T stands for Detailing, maintenance, and Painting. We would like the colors to be closer to the colors grey and light brown/khaki, but if there is any other suggestions that would go better with the design we are open to ideas.

Industry/Entity Type

Business

Contact Information for Business Card

Owner / Operator Owen Salcedo (555) 318-4927 / (555) 742- 0386

Font styles to use
Sans Serif

```html
<!DOCTYPE html>
<html lang="en">
<head>
<meta charset="utf-8">
<title>K.L.T Services – Business Cards</title>
<link href="https://fonts.googleapis.com/css2?family=Questrial&display=swap" rel="stylesheet">
<style>
  :root{
    --bg:#b9bbba;
    --card-dark:#2b2b2b;
    --card-light:#f2f2f2;
    --card-light-edge:#dcdcdc;
    --grey:#6b6c6e;
    --grey-text:#5a5b5d;
    --khaki:#a47c4b;
    --khaki-dark:#7d5c37;
    --white:#f4f4f4;
  }
  *{margin:0;padding:0;box-sizing:border-box}
  html,body{width:1200px;height:1048px;overflow:hidden}
  body{
    background:radial-gradient(ellipse at center,#d2d3d2 0%,var(--bg) 70%);
    font-family:"Questrial",sans-serif;
    position:relative;
  }
  .card{
    position:absolute;left:250px;width:700px;height:400px;
    border-radius:4px;overflow:hidden;
    box-shadow:0 10px 28px rgba(0,0,0,.28);
  }
  .card--back{top:92px;background:var(--card-dark);color:var(--white)}
  .card--front{top:556px;background:linear-gradient(160deg,#fbfbfb 0%,var(--card-light) 55%,var(--card-light-edge) 100%)}

  /* back */
  .services{position:absolute;left:70px;top:70px;list-style:none}
  .services li{display:flex;align-items:center;gap:12px;font-size:21px;line-height:34px;letter-spacing:.3px}
  .services svg{width:16px;height:16px;flex:none}

  .brand{position:absolute;display:flex;flex-direction:column}
  .brand__row{display:flex;align-items:center;gap:12px}
  .brand__mark{width:30px;height:30px;background:var(--khaki)}
  .brand__name{font-size:64px;line-height:1;letter-spacing:2px;color:var(--grey)}
  .brand__tagline{font-size:15px;color:var(--grey);margin-top:6px;letter-spacing:.2px}
  .card--back .brand{right:60px;top:170px;align-items:flex-end}
  .card--back .brand__name{color:#6e6f71}
  .card--front .brand{left:60px;top:90px}

  /* front */
  .contact{position:absolute;left:395px;top:86px;color:var(--grey-text)}
  .contact__name{font-size:34px;line-height:1.1}
  .contact__role{font-size:22px;color:var(--khaki);margin-bottom:18px}
  .contact__line{display:flex;align-items:center;gap:14px;font-size:23px;line-height:40px}
  .contact__line svg{width:26px;height:22px;flex:none}

  .band{position:absolute;bottom:0;height:82px}
  .band--grey{left:0;width:470px;background:var(--grey);clip-path:polygon(0 0,100% 0,96% 100%,0 100%)}
  .band--khaki{right:0;width:250px;background:linear-gradient(180deg,var(--khaki),var(--khaki-dark));clip-path:polygon(8% 0,100% 0,100% 100%,0 100%)}
</style>
</head>
<body>

<section class="card card--back" aria-label="Card back">
  <ul class="services">
    <li><svg viewBox="0 0 16 16"><path d="M2 8l4 4 8-9" fill="none" stroke="var(--khaki)" stroke-width="2.6"/></svg>Painting and Detailing</li>
    <li><svg viewBox="0 0 16 16"><path d="M2 8l4 4 8-9" fill="none" stroke="var(--khaki)" stroke-width="2.6"/></svg>Maintenance</li>
    <li><svg viewBox="0 0 16 16"><path d="M2 8l4 4 8-9" fill="none" stroke="var(--khaki)" stroke-width="2.6"/></svg>Sheetrock repairs</li>
    <li><svg viewBox="0 0 16 16"><path d="M2 8l4 4 8-9" fill="none" stroke="var(--khaki)" stroke-width="2.6"/></svg>Demolition</li>
    <li><svg viewBox="0 0 16 16"><path d="M2 8l4 4 8-9" fill="none" stroke="var(--khaki)" stroke-width="2.6"/></svg>Tile and Wood floors</li>
  </ul>
  <div class="brand">
    <div class="brand__row"><span class="brand__mark"></span><span class="brand__name">K.L.T</span></div>
    <span class="brand__tagline">Construction and home repair</span>
  </div>
</section>

<section class="card card--front" aria-label="Card front">
  <div class="brand">
    <div class="brand__row"><span class="brand__mark"></span><span class="brand__name">K.L.T</span></div>
    <span class="brand__tagline">Construction and home repair</span>
  </div>
  <div class="contact">
    <p class="contact__name">Owen Salcedo</p>
    <p class="contact__role">Owner / Operator</p>
    <p class="contact__line"><svg viewBox="0 0 26 22"><path d="M2 7c0-4 4-5 11-5s11 1 11 5l-5 1-1-3H8L7 8z M6 9h14l3 11H3z" fill="var(--khaki)"/><circle cx="13" cy="14" r="3" fill="var(--card-light)"/></svg>(555) 318-4927</p>
    <p class="contact__line"><svg viewBox="0 0 26 22"><path d="M2 7c0-4 4-5 11-5s11 1 11 5l-5 1-1-3H8L7 8z M6 9h14l3 11H3z" fill="var(--khaki)"/><circle cx="13" cy="14" r="3" fill="var(--card-light)"/></svg>(555) 742- 0386</p>
    <p class="contact__line"><svg viewBox="0 0 26 22"><rect x="1" y="3" width="24" height="16" fill="var(--khaki)"/><path d="M1 3l12 9 12-9" fill="none" stroke="var(--card-light)" stroke-width="1.6"/></svg>hello@kltservices.com</p>
  </div>
  <div class="band band--grey"></div>
  <div class="band band--khaki"></div>
</section>

</body>
</html>
```